Physician House Call Doctor

I need 2 newspaper color display adds. 1 small and 1 larger. I have attached some ideas but they need to be updated, more professional and eye-catching . I may also want to change the doctors picture and add some text. I need submit to newspaper in a PDF format and the adds must have a border.

```html
<!DOCTYPE html>
<html lang="en">
<head>
<meta charset="utf-8">
<title>Physician House Calls – Display Ad</title>
<link href="https://fonts.googleapis.com/css2?family=Open+Sans:wght@400;600;700;800&display=swap" rel="stylesheet">
<style>
  :root {
    --page-bg: #e9e6ec;
    --ink: #111111;
    --white: #ffffff;
    --title-grey: #e6e8ee;
    --accent-yellow: #f4f000;
    --accent-green: #1f7a3a;
    --doctor-blue: #1a6fb5;
    --phone-red: #d8141c;
    --band-blue: #2a8ad0;
    --footer-black: #1b1d22;
    --border: #0c0c10;
  }
  * { box-sizing: border-box; margin: 0; padding: 0; }
  html, body {
    width: 1200px; height: 730px; overflow: hidden;
    background: var(--page-bg);
    font-family: "Open Sans", Arial, sans-serif;
  }
  .ad {
    position: absolute; left: 333px; top: 20px;
    width: 533px; height: 690px;
    border: 2px solid var(--border);
    background: var(--white);
    overflow: hidden;
  }
  .hero {
    position: relative; height: 340px; color: var(--white);
    padding: 14px 18px 0 20px;
  }
  .hero-backdrop {
    position: absolute; inset: 0;
    background:
      radial-gradient(ellipse at 62% 45%, rgba(220,235,180,.55) 0%, rgba(90,170,110,.35) 25%, transparent 55%),
      linear-gradient(180deg, #1d2a8c 0%, #3b2f8f 28%, #1f6c86 55%, #2f7c4a 78%, #1c3f6a 100%);
  }
  .hero > *:not(.hero-backdrop) { position: relative; }
  .headline {
    color: var(--title-grey); font-weight: 700; line-height: .98;
    text-shadow: 0 2px 3px rgba(0,0,0,.5);
  }
  .headline .main { display: block; font-size: 45px; letter-spacing: -.3px; }
  .headline .sub { display: block; font-size: 33.5px; }
  .lead {
    margin-top: 20px; font-size: 16.5px; font-weight: 700; line-height: 1.05;
  }
  .promise {
    margin-top: 10px; color: var(--accent-yellow); font-weight: 800;
    font-size: 42px; line-height: .98; letter-spacing: -.3px;
    text-shadow: 0 2px 3px rgba(0,0,0,.45);
  }
  .area {
    margin-top: 12px; text-align: center; font-weight: 700; font-size: 19.5px;
  }
  .hours {
    margin-top: 6px; text-align: center; font-weight: 700; font-size: 17px; line-height: 1.18;
  }
  .details { position: relative; height: 309px; }
  .notice {
    position: absolute; left: 14px; top: 10px; z-index: 3;
    color: var(--accent-green); font-weight: 700; font-size: 14.8px;
  }
  .medicare {
    position: absolute; left: 14px; top: 38px; width: 340px; z-index: 3;
    font-weight: 700; font-size: 14.6px; line-height: .98; color: var(--ink);
  }
  .doctor-photo {
    position: absolute; right: 0; top: 40px; width: 258px; height: 269px;
    background:
      linear-gradient(90deg, rgba(255,255,255,1) 0%, rgba(255,255,255,0) 30%),
      linear-gradient(180deg, #d9dde2 0%, #c8cdd3 45%, #eef0f2 100%);
    z-index: 1;
  }
  .credentials {
    position: absolute; left: 30px; top: 70px; width: 300px; text-align: center;
    z-index: 3;
  }
  .credentials .name {
    color: var(--doctor-blue); font-weight: 700; font-size: 31px; line-height: 1;
  }
  .credentials .title {
    color: var(--doctor-blue); font-weight: 600; font-size: 17.5px; line-height: 1.25;
  }
  .credentials .summary {
    margin-top: 6px; color: var(--ink); font-size: 15px; line-height: 1.2;
  }
  .service-band {
    position: absolute; left: 0; top: 199px; width: 310px; height: 37px;
    background: linear-gradient(90deg, var(--band-blue) 0%, #4fa2dc 70%, rgba(120,185,230,.6) 100%);
    color: var(--white); font-weight: 700; font-size: 13.8px; line-height: 1;
    padding: 4px 0 0 16px; z-index: 2; white-space: nowrap;
  }
  .contact {
    position: absolute; left: 12px; top: 245px; z-index: 3;
    font-size: 19px; line-height: 1; color: var(--ink);
  }
  .contact .phone { color: var(--phone-red); font-weight: 700; }
  .contact .web { display: block; margin-left: 6px; color: var(--phone-red); font-weight: 700; font-size: 18.5px; }
  .contact .more { display: block; margin-left: 24px; }
  .footer-bar {
    position: absolute; left: 0; bottom: 0; width: 100%; height: 39px;
    background: var(--footer-black); color: var(--white);
    display: flex; align-items: center; justify-content: center;
    font-size: 14.5px; letter-spacing: 3.1px;
  }
</style>
</head>
<body>
  <div class="ad">
    <section class="hero">
      <div class="hero-backdrop" role="img" aria-label="Blue and green glowing background with a red stethoscope and a heartbeat line"></div>
      <h1 class="headline">
        <span class="main">Physician House Calls</span>
        <span class="sub">Affordable and Convenient</span>
      </h1>
      <p class="lead">Can’t get to the doctor or<br>your doctor can’t see you right away,</p>
      <p class="promise">Dr. Whitford<br>will come to you.</p>
      <p class="area">He is Lakeside Village and the surrounding area!</p>
      <p class="hours">Convenient Daytime Hours and<br>Open most evenings, weekends, and holidays!</p>
    </section>

    <section class="details">
      <p class="notice">Medicinal Marijuana recommendation is now available in Maryland.</p>
      <p class="medicare">Medicare is accepted for qualified patients,<br>you pay a small trip fee for your house call.</p>
      <div class="doctor-photo" role="img" aria-label="Portrait photo of the physician in a white coat with a stethoscope"></div>
      <div class="credentials">
        <p class="name">Daniel R. Whitford,</p>
        <p class="title">MD Primary and Urgent Care</p>
        <p class="title">Board Certified Family Medicine</p>
        <p class="summary">Dr. Whitford does family consults, second opinions medical testing and evaluations .</p>
      </div>
      <p class="service-band">We also offer Lab Testing, X-rays Breathing<br>Treatments all in the comfort of your home.</p>
      <p class="contact">
        Call: <span class="phone">202-555-0147</span> or visit
        <span class="web">www.capitolhousemed.com</span>
        <span class="more">for more information.</span>
      </p>
    </section>

    <p class="footer-bar">Keep this advertisement handy for future reference.</p>
  </div>
</body>
</html>
```